Multivitamin fruit drink in tetrapak

Label design for a 200 ml tetrapak which contains fruit juice with multivitamins in natural form . Product will be promoted to doctors and will follow a otx model. The target is children and women. Being a completely natural fortified multivitamin and mineral drink , the natural aspects to be highlighted. A white background is suggestive . Should not have more than 6 colors as this involves flexo printing.

Target Market(s)

Children and women through doctors recommendations

Industry/Entity Type

Pharmaceutical

Font styles to use
Serif
Sans Serif
Decorative

Requirements
Must have
• Pictures of fruit . Variant 1 is mango and variant 2 is orange. Brand name is Verosta. Can also suggest new names.
Nice to have
• The brand standing out, with white or softer color background
Should not have
• Should not have Dark background. Not funky or too colorful.

```html
<!DOCTYPE html>
<html lang="en">
<head>
<meta charset="utf-8">
<title>Verosta Mango Fruit Juice – Carton Panels</title>
<link rel="stylesheet" href="https://fonts.googleapis.com/css2?family=Ubuntu:wght@400;500;700&display=swap">
<style>
  :root {
    --backdrop: #ececec;
    --panel-white: #ffffff;
    --side-white: #f7f7f7;
    --band-gold: #d9a334;
    --ink: #1f1f1f;
    --ink-soft: #2a2a2a;
    --ink-muted: #6a6a6a;
    --fruit-red: #d9432c;
    --fruit-orange: #eea23a;
    --fruit-yellow: #f5cf45;
  }
  * { margin: 0; padding: 0; box-sizing: border-box; }
  html, body {
    width: 1200px;
    height: 2240px;
    overflow: hidden;
    background: var(--backdrop);
  }
  .canvas {
    position: relative;
    width: 1200px;
    height: 2240px;
    font-family: "Ubuntu", sans-serif;
  }
  .front-panel {
    position: absolute;
    left: 90px;
    top: 80px;
    width: 720px;
    height: 2080px;
    background: var(--panel-white);
    overflow: hidden;
    color: var(--ink);
  }
  .side-panel {
    position: absolute;
    left: 810px;
    top: 80px;
    width: 300px;
    height: 2080px;
    background: var(--side-white);
    border-left: 1px solid #e2e2e2;
    overflow: hidden;
  }
  .band {
    position: absolute;
    left: 0;
    width: 100%;
  }
  .band--top { top: 0; height: 250px; }
  .band--bottom { bottom: 0; height: 340px; }

  .brand-name {
    position: absolute;
    top: 330px;
    left: 0;
    width: 100%;
    text-align: center;
    font-weight: 400;
    font-size: 96px;
    letter-spacing: 6px;
    line-height: 1;
    color: var(--ink);
  }
  .claim {
    position: absolute;
    top: 480px;
    left: 0;
    width: 100%;
    text-align: center;
    font-weight: 400;
    font-size: 44px;
    line-height: 1.2;
    color: var(--ink-soft);
  }
  .flavour {
    position: absolute;
    top: 760px;
    left: 0;
    width: 100%;
    text-align: center;
    line-height: 1;
  }
  .flavour__name {
    display: block;
    font-weight: 700;
    font-size: 100px;
    color: var(--ink);
  }
  .flavour__type {
    display: block;
    margin-top: 10px;
    font-weight: 400;
    font-size: 56px;
    color: var(--ink-soft);
  }
  .fruit-illustration {
    position: absolute;
    left: 0;
    top: 960px;
    width: 720px;
    height: 860px;
    background: linear-gradient(150deg, var(--fruit-red) 10%, var(--fruit-orange) 50%, var(--fruit-yellow) 85%);
    opacity: 0.9;
  }
  .volume {
    position: absolute;
    bottom: 110px;
    left: 0;
    width: 100%;
    text-align: center;
    font-weight: 400;
    font-size: 50px;
    color: var(--panel-white);
    line-height: 1;
  }
  .info-block {
    position: absolute;
    left: 34px;
    width: 232px;
    text-align: center;
    font-size: 19px;
    line-height: 1.55;
    color: var(--ink-muted);
  }
  .info-block--about { top: 410px; }
  .info-block--ingredients { top: 800px; }
  .info-block--usage { top: 1190px; }
  .info-block--storage { top: 1530px; }
</style>
</head>
<body>
  <main class="canvas">
    <section class="front-panel">
      <svg class="band band--top" viewBox="0 0 720 250" preserveAspectRatio="none" aria-hidden="true">
        <path d="M0 0 H720 V150 C620 130 520 170 400 190 C260 212 130 222 0 208 Z" fill="var(--band-gold)"/>
      </svg>

      <h1 class="brand-name">VEROSTA</h1>
      <p class="claim">Fortified with multivitamins<br>and minerals</p>

      <h2 class="flavour">
        <span class="flavour__name">mango</span>
        <span class="flavour__type">fruit juice</span>
      </h2>

      <div class="fruit-illustration" role="img" aria-label="Photograph of a ripe red and yellow mango with a green leaf, mango slices and golden juice drops"></div>

      <svg class="band band--bottom" viewBox="0 0 720 340" preserveAspectRatio="none" aria-hidden="true">
        <path d="M0 70 C140 40 260 80 390 88 C520 96 620 50 720 30 V340 H0 Z" fill="var(--band-gold)"/>
      </svg>
      <p class="volume">200ml</p>
    </section>

    <aside class="side-panel">
      <p class="info-block info-block--about">Made from ripe mangoes picked at peak season, blended with natural vitamins and minerals for daily care. Serve chilled and shake well before use.</p>
      <p class="info-block info-block--ingredients">Ingredients: water, mango pulp, natural fruit sugars, vitamin C, vitamin A, vitamin E, B vitamins, zinc, iron and calcium. No artificial colours, flavours or preservatives are added to this drink.</p>
      <p class="info-block info-block--usage">Recommended for children and women as part of a balanced diet. Ask your doctor about daily intake. Store in a cool, dry place away from direct sunlight.</p>
      <p class="info-block info-block--storage">Once opened, keep refrigerated and consume within two days. Best before date and batch number are printed on top of the pack. Packed under hygienic conditions in an aseptic carton.</p>
    </aside>
  </main>
</body>
</html>
```